Eye catchy Construction Development business cards and stationery
Torvane Arch
Modern
Your Name
Managing Director
11111 My Street suite #100 City, STATE 66211
myemail@email.com
www.mywebsite.com
Use my winning logo from here http://www.plumvexstudio.com/contests/logo-for-construction-developer-company
Some elegant but modern design. One idea would be to use the company logo printed on silver metallic look, such as http://www.plumvexstudio.com/contests/theoakhearth-logo-project

```html
<!DOCTYPE html>
<html lang="en">
<head>
<meta charset="utf-8">
<title>Torvane Arch – Business Cards</title>
<link href="https://fonts.googleapis.com/css2?family=Montserrat:wght@400;600;700&family=Open+Sans:wght@400;600&display=swap" rel="stylesheet">
<style>
  :root{
    --bg:#d9d9d9;
    --card:#ffffff;
    --blue:#1f8fb8;
    --orange:#f39a1e;
    --ink:#2a2a2a;
    --muted:#555;
  }
  *{box-sizing:border-box;margin:0;padding:0}
  html,body{width:1200px;height:878px;overflow:hidden;background:var(--bg)}
  .stage{position:relative;width:1200px;height:878px}
  .card{position:absolute;width:620px;height:354px;background:var(--card);
    box-shadow:0 6px 18px rgba(0,0,0,.18);overflow:hidden}
  .card--front{left:290px;top:52px}
  .card--back{left:290px;top:472px}

  .brand{display:flex;align-items:center;gap:12px;font-family:"Montserrat",sans-serif;
    font-weight:700;color:var(--blue);letter-spacing:.5px}
  .brand__dot{width:22px;height:22px;background:var(--orange);border-radius:50%}
  .card--front .brand{position:absolute;left:0;right:0;top:0;bottom:0;justify-content:center;font-size:38px}
  .card--back .brand{position:absolute;left:40px;top:62px;font-size:30px}

  .waves{position:absolute;left:0;top:0;width:620px;height:354px}
  .website{position:absolute;left:30px;top:300px;font-family:"Open Sans",sans-serif;
    font-size:12px;color:#fff;letter-spacing:.6px;transform:rotate(8deg);transform-origin:left center}

  .contact{position:absolute;left:380px;top:92px;font-family:"Open Sans",sans-serif;color:var(--muted)}
  .contact__name{font-family:"Montserrat",sans-serif;font-weight:700;font-size:17px;color:var(--ink)}
  .contact__title{font-size:11.5px;color:var(--orange);margin-top:2px;margin-bottom:10px}
  .contact__line{display:flex;align-items:center;gap:7px;font-size:11px;line-height:17px}
  .contact__line svg{width:10px;height:10px;flex:none;fill:var(--orange)}
  .contact__addr{font-size:11px;line-height:15px;margin-bottom:4px;padding-left:17px}
</style>
</head>
<body>
<main class="stage">

  <section class="card card--front" aria-label="Business card front">
    <div class="brand"><span class="brand__dot"></span>Torvane Arch</div>
  </section>

  <section class="card card--back" aria-label="Business card back">
    <svg class="waves" viewBox="0 0 620 354" aria-hidden="true">
      <path d="M0 215 C220 225 430 300 620 352 L620 362 C430 312 220 237 0 227 Z" fill="var(--orange)"/>
      <path d="M0 240 C200 252 380 300 520 354 L0 354 Z" fill="var(--blue)"/>
    </svg>
    <div class="brand"><span class="brand__dot"></span>Torvane Arch</div>
    <p class="website">www.yourwebsitename.com</p>

    <div class="contact">
      <p class="contact__name">Dana Whitlock</p>
      <p class="contact__title">Managing Director</p>
      <p class="contact__addr">210 Harlow Street<br>Sample City Country 324</p>
      <p class="contact__line"><svg viewBox="0 0 10 10"><path d="M2 0h2l1 3-1.5 1a6 6 0 0 0 2.5 2.5L7 5l3 1v2a2 2 0 0 1-2 2A8 8 0 0 1 0 2a2 2 0 0 1 2-2z"/></svg>123 456 7890</p>
      <p class="contact__line"><svg viewBox="0 0 10 10"><rect x="2" y="0" width="6" height="10" rx="1"/></svg>123 456 7890</p>
      <p class="contact__line"><svg viewBox="0 0 10 10"><rect x="0" y="3" width="10" height="5"/><rect x="2" y="0" width="6" height="3"/></svg>123 456 7890</p>
      <p class="contact__line"><svg viewBox="0 0 10 10"><path d="M0 2h10v6H0z"/></svg>yourname.com</p>
      <p class="contact__line"><svg viewBox="0 0 10 10"><circle cx="5" cy="5" r="5"/></svg>www.yourname.com</p>
    </div>
  </section>

</main>
</body>
</html>
```